Harbor Peak Advisory (Construction Company) On Site Signage

hoping to get a 2ft wide by 4ft tall sign design that will be place on construction sites with our name, wordage with a mountain background and river like drawing below. Sign will be CNC metal cutout so not a ton of detail. Black and White design

```html
<!DOCTYPE html>
<html lang="en">
<head>
<meta charset="UTF-8">
<title>Harbor Peak Advisory – Site Sign</title>
<link href="https://fonts.googleapis.com/css2?family=Montserrat:wght@700;800&family=Oswald:wght@700&display=swap" rel="stylesheet">
<style>
  :root {
    --page: #e6e6e6;
    --metal-dark: #333333;
    --metal-light: #606060;
    --ink: #353535;
    --cut: #e6e6e6;
  }
  html, body {
    margin: 0;
    width: 1200px;
    height: 1200px;
    overflow: hidden;
    background: var(--page);
  }
  .canvas {
    position: relative;
    width: 1200px;
    height: 1200px;
  }
  .sign {
    position: absolute;
    left: 294px;
    top: 120px;
    width: 596px;
    height: 970px;
    overflow: hidden;
    background: linear-gradient(150deg,
      var(--metal-light) 0%, var(--metal-dark) 14%, var(--metal-dark) 20%,
      var(--metal-light) 34%, var(--metal-dark) 48%, var(--metal-light) 62%,
      var(--metal-dark) 76%, var(--metal-light) 86%, var(--metal-dark) 100%);
  }
  .name-band {
    position: absolute;
    left: 7px;
    top: 111px;
    width: 581px;
    height: 68px;
    background: var(--cut);
    display: flex;
    align-items: center;
    justify-content: center;
  }
  .company-name {
    font-family: "Montserrat", sans-serif;
    font-weight: 700;
    font-size: 58px;
    color: var(--ink);
    letter-spacing: 1px;
    line-height: 1;
  }
  .scene-art {
    position: absolute;
    left: 27px;
    top: 258px;
    width: 557px;
    height: 326px;
    background: radial-gradient(ellipse at 50% 60%, #d8d8d8 0%, #9a9a9a 55%, rgba(90,90,90,0) 80%);
    border-radius: 4px;
  }
  .rule {
    position: absolute;
    left: 25px;
    width: 544px;
    height: 4px;
    background: var(--cut);
  }
  .rule.top { top: 593px; }
  .rule.bottom { top: 657px; }
  .tagline {
    position: absolute;
    left: 25px;
    top: 603px;
    width: 544px;
    text-align: center;
    font-family: "Oswald", sans-serif;
    font-weight: 700;
    font-size: 34px;
    line-height: 50px;
    color: var(--cut);
    white-space: nowrap;
  }
  .website {
    position: absolute;
    left: 0;
    top: 704px;
    width: 596px;
    text-align: center;
    font-family: "Montserrat", sans-serif;
    font-weight: 800;
    font-size: 32px;
    line-height: 40px;
    color: var(--cut);
    letter-spacing: 1px;
    white-space: nowrap;
  }
  .phone-band {
    position: absolute;
    left: 7px;
    top: 756px;
    width: 581px;
    height: 102px;
    background: var(--cut);
    display: flex;
    align-items: center;
    justify-content: center;
    gap: 12px;
  }
  .phone-icon { width: 60px; height: 60px; flex: none; }
  .phone-number {
    font-family: "Montserrat", sans-serif;
    font-weight: 800;
    font-size: 54px;
    color: var(--ink);
    line-height: 1;
    white-space: nowrap;
  }
</style>
</head>
<body>
<div class="canvas">
  <div class="sign">
    <div class="name-band"><span class="company-name">HARBOR PEAK</span></div>

    <div class="scene-art" role="img" aria-label="Cut-out illustration of mountain peaks with pine trees on both sides and a modern two-storey house in front"></div>

    <div class="rule top"></div>
    <div class="tagline">CONSULT • CONTRACT • CONSTRUCT</div>
    <div class="rule bottom"></div>

    <div class="website">WWW.HARBORPEAK.COM</div>

    <div class="phone-band">
      <svg class="phone-icon" viewBox="0 0 60 60" aria-hidden="true">
        <circle cx="30" cy="30" r="30" fill="#353535"/>
        <path d="M20 15c2-1 4 0 5 2l3 6c1 2 0 3-1 4l-2 2c1 4 4 7 8 9l2-2c1-1 2-2 4-1l6 3c2 1 3 3 2 5l-2 3c-2 2-5 2-8 1-10-4-17-11-21-21-1-3-1-6 1-8z" fill="#e6e6e6"/>
      </svg>
      <span class="phone-number">(970) 555-0142</span>
    </div>
  </div>
</div>
</body>
</html>
```